quiet meadow therapy (QMT)

I need to build a website for my therapy business.
There are two parts to the website
on the landing page; they choose whether they are therapists making a referral or patients needing more information.
After that, they are taken to their respective pages.
There is the textual information and a referral form on the therapist page, and on the patient page, the text is a bit different, and there will be a booking page on the patient page.
Visually minimal, it's a therapeutic website. I want it clean, clinical, and modern
colors: greenish blue or maybe orangish
PHP/html code
Updates

Hi everyone
I'm very sorry for the lack of responses to your designs. I am trying to work it out, but this platform has been a challenge for me.
I appreciate everyone's efforts, and I am unsure how to rate designs and move forward with the ones I like. There is a 5-star rating, but I don't understand how I'm supposed to politely say that it is not it without feeling like I'm going to affect someone's future rating negatively.
Please understand me. Thank you

Designs look the same

Target Market(s)

therapy and stress management

Industry/Entity Type

stress management therapy

Coding

Coded - Design and coding required

Number of Pages Required

5+ page

Font styles to use
Serif

Colors
0094D4
00A9DD
6FCCEA
C7EBF8
E9F6FB
00AB8E
00BBA5
67D7C9
C6EFE9
E9F9F6

Requirements
Must have
• landing page that that have 2 options. one for therapist another for patient

```html
<!DOCTYPE html>
<html lang="en">
<head>
<meta charset="utf-8">
<title>Quiet Meadow Therapy</title>
<link href="https://fonts.googleapis.com/css2?family=Open+Sans:wght@400;600;700;800&display=swap" rel="stylesheet">
<style>
:root{
  --teal:#13a594;
  --teal-deep:#0f9484;
  --orange:#f7931e;
  --ink:#111;
  --text:#555;
  --mist:#ecf1f1;
  --white:#fff;
}
*{box-sizing:border-box;margin:0;padding:0}
html,body{width:1200px;height:3056px;overflow:hidden}
body{position:relative;font-family:"Open Sans",sans-serif;color:var(--ink);background:var(--white)}
.abs{position:absolute}

/* header */
.site-header{position:absolute;left:0;top:0;width:1200px;height:115px;background:var(--white);z-index:3}
.brand{position:absolute;display:flex;flex-direction:column}
.brand-row{display:flex;align-items:center;gap:10px}
.brand-dot{width:30px;height:30px;border-radius:50%;background:var(--teal)}
.brand-letters{font-size:38px;font-weight:600;letter-spacing:14px;color:#222;line-height:1}
.brand-tag{font-size:8px;font-weight:700;letter-spacing:1.6px;color:var(--orange);margin-top:6px}
.main-nav{position:absolute;top:47px;left:0;font-size:14px;color:#222}
.main-nav a{position:absolute;white-space:nowrap;color:inherit;text-decoration:none}
.main-nav a.active{color:var(--teal);font-weight:600}
.nav-dot{position:absolute;left:404px;top:73px;width:6px;height:6px;border-radius:50%;background:var(--teal)}
.btn-contact{position:absolute;left:892px;top:38px;width:135px;height:39px;background:var(--orange);color:#fff;font-size:14px;display:flex;align-items:center;justify-content:center;border-radius:2px 12px 2px 12px}

/* hero: path choice for therapists and patients */
.hero{position:absolute;left:0;top:115px;width:1200px;height:640px;background:linear-gradient(90deg,#e7e7e7 0%,#dcdcdc 50%,#cfcfcf 100%);overflow:hidden}
.hero-photo{position:absolute;left:620px;top:0;width:580px;height:640px;background:linear-gradient(100deg,rgba(220,220,220,0) 0%,#c9c3bd 25%,#d8b8a4 50%,#c9c9c9 75%,#bdbdbd 100%)}
.hero-title{position:absolute;left:172px;top:125px;font-size:53px;font-weight:800;line-height:56px;letter-spacing:0.5px}
.hero-title .accent{color:var(--orange)}
.hero-lead{position:absolute;left:172px;top:306px;width:370px;font-size:14.5px;line-height:22px;color:#444}
.btn{position:absolute;display:flex;align-items:center;justify-content:center;gap:6px;font-size:12px;font-weight:700;text-transform:uppercase;white-space:nowrap}
.btn-solid{background:var(--teal);color:#fff;border-radius:2px 14px 2px 14px}
.btn-outline{border:1.5px solid var(--orange);color:var(--orange);border-radius:2px 14px 2px 14px}
.waves{position:absolute;left:0;top:0;pointer-events:none}

/* what we do */
.section-title{position:absolute;left:0;width:1200px;text-align:center;font-weight:700;font-size:37px}
.section-lead{position:absolute;left:270px;width:660px;text-align:center;font-size:14px;line-height:22px;color:#555}
.service-card{position:absolute;top:949px;width:273px;height:263px;background:#fff;border-top:3px solid var(--teal);border-bottom:3px solid var(--teal);border-radius:22px 0 22px 0;box-shadow:0 6px 18px rgba(0,0,0,.08);text-align:center}
.service-card.highlight{border-color:var(--orange)}
.service-card svg{margin-top:30px}
.service-card h3{font-size:18px;font-weight:700;margin-top:16px;letter-spacing:.3px}
.service-card.highlight h3{color:var(--orange)}
.service-card p{font-size:10px;line-height:16px;color:#666;width:200px;margin:14px auto 0}

/* challenge band */
.challenge{position:absolute;left:0;top:1293px;width:1200px;height:355px;background:var(--teal-deep)}
.challenge h2{position:absolute;top:73px;left:0;width:1200px;text-align:center;color:#fff;font-size:38px;font-weight:700}
.challenge p{position:absolute;top:140px;left:250px;width:700px;text-align:center;color:#fff;font-size:14px;line-height:19px}
.btn-light{position:absolute;left:500px;top:193px;width:200px;height:36px;background:#fff;color:var(--teal);font-size:11.5px;font-weight:600;display:flex;align-items:center;justify-content:center;gap:6px;border-radius:2px 14px 2px 14px}
.mist{position:absolute;left:0;top:1648px;width:1200px;height:700px;background:var(--mist)}
.partners{position:absolute;left:172px;top:1592px;width:855px;height:113px;background:#fff;border-bottom:3px solid var(--teal);border-radius:0 0 22px 0;box-shadow:0 6px 18px rgba(0,0,0,.08);display:flex;align-items:center;justify-content:space-around;padding:0 20px}
.partner-name{font-size:23px;font-weight:800;color:#222;display:flex;align-items:center;gap:8px}
.partner-mark{width:16px;height:16px;background:#222}
.partner-mark.round{border-radius:50%}

/* why choose */
.why-photo{position:absolute;left:178px;top:1803px;width:380px;height:380px;border-radius:50%;background:radial-gradient(circle at 40% 45%,#c8895a 0%,#8a6a4a 35%,#5d6b4f 70%,#3f4d3a 100%)}
.badge{position:absolute;border-radius:50%;display:flex;align-items:center;justify-content:center}
.badge-teal{left:176px;top:1783px;width:134px;height:134px;background:var(--mist)}
.badge-teal span{width:112px;height:112px;border-radius:50%;background:var(--teal);display:flex;align-items:center;justify-content:center}
.badge-white{left:423px;top:2046px;width:134px;height:134px;background:var(--mist)}
.badge-white span{width:112px;height:112px;border-radius:50%;background:#fff;display:flex;align-items:center;justify-content:center}
.eyebrow{position:absolute;font-size:14px;letter-spacing:1px;color:#222}
.why-title{position:absolute;left:607px;top:1835px;font-size:38px;font-weight:700}
.why-text{position:absolute;left:607px;top:1892px;width:380px;font-size:12.2px;line-height:22px;letter-spacing:1px;color:#333}

/* testimonials */
.clients{position:absolute;left:0;top:2200px;width:1200px;height:519px}
.clients-eyebrow{position:absolute;top:2383px;left:0;width:1200px;text-align:center;color:#fff;font-size:14px;letter-spacing:4px}
.clients-title{position:absolute;top:2410px;left:0;width:1200px;text-align:center;color:#fff;font-size:38px;font-weight:700}
.review{position:absolute;top:2511px;width:200px;height:147px;background:#fff;border-radius:0 0 18px 0;text-align:center}
.review .avatar{width:40px;height:40px;border-radius:50%;margin:16px auto 0;background:radial-gradient(circle,#8a6a52,#d2c4b4)}
.review h4{font-size:12px;font-weight:600;margin-top:8px}
.review p{font-size:7.5px;line-height:12px;color:#666;width:130px;margin:6px auto 0}
.review svg{margin-top:6px}

/* footer */
.site-footer{position:absolute;left:0;top:2719px;width:1200px;height:337px;background:var(--mist)}
.footer-about{position:absolute;left:172px;top:2864px;width:360px;font-size:10px;line-height:19px;color:#444}
.social{position:absolute;top:2935px;width:30px;height:30px;border-radius:50%;border:1.5px solid var(--teal)}
.footer-head{position:absolute;top:2797px;font-size:20px;font-weight:700}
.footer-list{position:absolute;list-style:none;font-size:10.5px;color:#333}
.footer-list li{height:26px;display:flex;align-items:center;gap:10px}
.footer-list svg{flex:none}
.subscribe{position:absolute;left:869px;top:2941px;width:158px;height:24px;background:#fff;border-radius:12px;font-size:7.5px;color:#999;display:flex;align-items:center;padding-left:12px}
.subscribe b{position:absolute;right:-2px;top:-1px;width:25px;height:25px;border-radius:50%;background:var(--teal);color:#fff;font-weight:400;font-size:9px;display:flex;align-items:center;justify-content:center}
.footer-rule{position:absolute;left:172px;top:3003px;width:855px;height:1px;background:#c9d2d2}
.copyright{position:absolute;top:3022px;left:0;width:1200px;text-align:center;font-size:10px;color:#777}
</style>
</head>
<body>

<header class="site-header">
  <div class="brand" style="left:173px;top:26px">
    <div class="brand-row"><span class="brand-dot"></span><span class="brand-letters">QMT</span></div>
    <span class="brand-tag">QUIET MEADOW THERAPY</span>
  </div>
  <nav class="main-nav">
    <a class="active" style="left:385px">HOME</a>
    <a style="left:478px">ABOUT</a>
    <a style="left:574px">SERVICES</a>
    <a style="left:684px">PAGES</a>
    <a style="left:777px">BLOG</a>
  </nav>
  <span class="nav-dot"></span>
  <span class="btn-contact">CONTACT US</span>
</header>

<section class="hero">
  <div class="hero-photo" role="img" aria-label="Therapist gently supporting a patient's head and neck during a session"></div>
  <h1 class="hero-title">QUIET<br><span class="accent">MEADOW</span><br>THERAPY</h1>
  <p class="hero-lead">Choose your path: therapists can make a referral, patients can learn more and book a session.</p>
  <a class="btn btn-solid path-therapist" style="left:172px;top:376px;width:164px;height:38px">For Therapists
    <svg width="11" height="11" viewBox="0 0 12 12"><path d="M1 6h9M6 2l4 4-4 4" stroke="#fff" stroke-width="1.5" fill="none"/></svg></a>
  <a class="btn btn-outline path-patient" style="left:355px;top:376px;width:163px;height:38px">For Patients
    <svg width="11" height="11" viewBox="0 0 12 12"><path d="M1 6h9M6 2l4 4-4 4" stroke="#f7931e" stroke-width="1.5" fill="none"/></svg></a>
</section>

<svg class="waves" width="1200" height="800" viewBox="0 0 1200 800" aria-hidden="true">
  <path d="M0 697 C200 655 400 655 640 705 C850 745 1050 720 1200 690 L1200 800 L0 800 Z" fill="#fff"/>
  <path d="M0 648 C150 600 300 570 460 600 C640 635 800 745 1010 786 C1090 795 1150 786 1200 776" stroke="#f7931e" stroke-width="3" fill="none"/>
</svg>

<h2 class="section-title" style="top:804px">What We Do</h2>
<p class="section-lead" style="top:855px">Amet minim mollit non deserunt ullamco est sit aliqua dolor do amet sint. Velit officia consequat duis enim velit mollit. Exercitation veniam consequat sunt nostrud amet.</p>

<article class="service-card" style="left:172px">
  <svg width="90" height="70" viewBox="0 0 90 70" aria-hidden="true"><path d="M45 8 C30 25 30 45 45 62 C60 45 60 25 45 8 Z M45 62 C25 60 10 48 8 32 C25 34 38 45 45 62 M45 62 C65 60 80 48 82 32 C65 34 52 45 45 62" stroke="#13a594" stroke-width="3" fill="none"/></svg>
  <h3>STRESS THERAPY</h3>
  <p>Amet minim mollit non deserunt ullamco est sit aliqua dolor do amet sint. Velit officia consequat duis enim velit mollit. Exercitation veniam consequat sunt nostrud amet.</p>
</article>
<article class="service-card highlight" style="left:463px">
  <svg width="90" height="70" viewBox="0 0 90 70" aria-hidden="true"><circle cx="45" cy="35" r="14" stroke="#f7931e" stroke-width="3" fill="none"/><path d="M45 6v9M45 55v9M16 35h9M65 35h9M24 14l6 6M60 50l6 6M66 14l-6 6M30 50l-6 6" stroke="#f7931e" stroke-width="3"/></svg>
  <h3>DEPRESSION THERAPY</h3>
  <p>Amet minim mollit non deserunt ullamco est sit aliqua dolor do amet sint. Velit officia consequat duis enim velit mollit. Exercitation veniam consequat sunt nostrud amet.</p>
</article>
<article class="service-card" style="left:754px">
  <svg width="90" height="70" viewBox="0 0 90 70" aria-hidden="true"><path d="M15 12h60v36H42l-14 12V48H15Z" stroke="#13a594" stroke-width="3" fill="none" stroke-linejoin="round"/><path d="M28 26h34M28 35h22" stroke="#13a594" stroke-width="3"/></svg>
  <h3>PATIENT COUNSELING</h3>
  <p>Amet minim mollit non deserunt ullamco est sit aliqua dolor do amet sint. Velit officia consequat duis enim velit mollit. Exercitation veniam consequat sunt nostrud amet.</p>
</article>

<section class="challenge">
  <h2>We are Always Ready For A Challenge</h2>
  <p>Amet minim mollit non deserunt ullamco est sit aliqua dolor do amet sint. Velit officia consequat duis enim velit mollit. Exercitation veniam consequat sunt nostrud amet.</p>
  <span class="btn-light">BOOK AN APPOINTMENT
    <svg width="11" height="11" viewBox="0 0 12 12"><path d="M1 6h9M6 2l4 4-4 4" stroke="#13a594" stroke-width="1.5" fill="none"/></svg></span>
</section>

<div class="mist"></div>

<div class="partners">
  <span class="partner-name"><span class="partner-mark"></span>NORTHPEAK</span>
  <span class="partner-name"><span class="partner-mark round"></span>lumenform</span>
  <span class="partner-name"><span class="partner-mark"></span>lumenform</span>
  <span class="partner-name"><span class="partner-mark round"></span>NORTHPEAK</span>
</div>

<div class="why-photo" role="img" aria-label="Smiling father holding his laughing young child outdoors"></div>
<div class="badge badge-teal"><span>
  <svg width="62" height="56" viewBox="0 0 24 22"><path d="M12 21 C5 15 1 11 1 6.5 C1 3.4 3.4 1 6.5 1 C8.6 1 10.8 2.2 12 4 C13.2 2.2 15.4 1 17.5 1 C20.6 1 23 3.4 23 6.5 C23 11 19 15 12 21Z" fill="#fff"/></svg>
</span></div>
<div class="badge badge-white"><span>
  <svg width="58" height="52" viewBox="0 0 24 22"><path d="M12 21 C5 15 1 11 1 6.5 C1 3.4 3.4 1 6.5 1 C8.6 1 10.8 2.2 12 4 C13.2 2.2 15.4 1 17.5 1 C20.6 1 23 3.4 23 6.5 C23 11 19 15 12 21Z" fill="#13a594"/></svg>
</span></div>

<span class="eyebrow" style="left:607px;top:1812px">WHY WE ARE</span>
<h2 class="why-title">Why Choose Us</h2>
<p class="why-text">Lorem Ipsum is simply dummy text of the printing and typesetting industry. Lorem Ipsum has been the industry's standard dummy text ever since the 1500s, when an unknown printer took a galley of type and scrambled it to make a type specimen book. It has survived not only five centuries, but also the leap into electronic typesetting, remaining essentially unchanged. It was popularised in the 1960s with the release of Letraset sheets containing Lorem Ipsum passages, and more recently with desktop publishing.</p>
<span class="btn btn-solid" style="left:607px;top:2134px;width:128px;height:37px;font-weight:600">Book Now
  <svg width="11" height="11" viewBox="0 0 12 12"><path d="M1 6h9M6 2l4 4-4 4" stroke="#fff" stroke-width="1.5" fill="none"/></svg></span>

<svg class="clients" viewBox="0 0 1200 519" aria-hidden="true">
  <path d="M0 100 C180 75 380 50 520 68 C700 92 850 125 1020 115 C1100 110 1160 103 1200 97 L1200 519 L0 519 Z" fill="#0f9484"/>
  <path d="M0 219 C80 120 200 60 360 47 C520 35 620 75 760 100 C900 125 1080 115 1200 0" stroke="#f7931e" stroke-width="3" fill="none"/>
</svg>
<p class="clients-eyebrow">TESTIMONIALS</p>
<h2 class="clients-title">Our Happy Clients</h2>
<svg class="abs" style="left:490px;top:2470px" width="220" height="14" viewBox="0 0 220 14" aria-hidden="true"><path d="M0 7h100M120 7h100" stroke="#fff" stroke-width="1.5"/><circle cx="110" cy="7" r="5.5" fill="#fff"/></svg>

<article class="review" style="left:245px">
  <div class="avatar" role="img" aria-label="Client portrait"></div>
  <h4>Ren Calloway</h4>
  <p>"Amet minim mollit non deserunt ullamco est sit"</p>
  <svg width="80" height="14" viewBox="0 0 80 14" aria-hidden="true"><g fill="#f5b800"><path id="st" d="M7 0l2 4.6 5 .4-3.8 3.3 1.2 4.9L7 10.6 2.6 13.2l1.2-4.9L0 5l5-.4Z"/><use href="#st" x="16"/><use href="#st" x="32"/><use href="#st" x="48"/><use href="#st" x="64"/></g></svg>
</article>
<article class="review" style="left:500px">
  <div class="avatar" role="img" aria-label="Client portrait"></div>
  <h4>Ren Calloway</h4>
  <p>"Amet minim mollit non deserunt ullamco est sit"</p>
  <svg width="80" height="14" viewBox="0 0 80 14" aria-hidden="true"><g fill="#f5b800"><use href="#st"/><use href="#st" x="16"/><use href="#st" x="32"/><use href="#st" x="48"/><use href="#st" x="64"/></g></svg>
</article>
<article class="review" style="left:755px">
  <div class="avatar" role="img" aria-label="Client portrait"></div>
  <h4>Ren Calloway</h4>
  <p>"Amet minim mollit non deserunt ullamco est sit"</p>
  <svg width="80" height="14" viewBox="0 0 80 14" aria-hidden="true"><g fill="#f5b800"><use href="#st"/><use href="#st" x="16"/><use href="#st" x="32"/><use href="#st" x="48"/><use href="#st" x="64"/></g></svg>
</article>

<footer class="site-footer"></footer>
<div class="brand" style="left:173px;top:2797px">
  <div class="brand-row"><span class="brand-dot"></span><span class="brand-letters">QMT</span></div>
  <span class="brand-tag">QUIET MEADOW THERAPY</span>
</div>
<p class="footer-about">Amet minim mollit non deserunt ullamco est sit aliqua dolor do amet sint. Velit officia consequat duis enim velit mollit. Exercitation veniam consequat sunt nostrud amet.</p>
<span class="social" style="left:172px" aria-label="Social profile"></span>
<span class="social" style="left:219px" aria-label="Social profile"></span>
<span class="social" style="left:266px" aria-label="Social profile"></span>

<h3 class="footer-head" style="left:634px">Useful Links</h3>
<ul class="footer-list" style="left:634px;top:2842px">
  <li><svg width="9" height="9" viewBox="0 0 12 12"><path d="M1 6h9M6 2l4 4-4 4" stroke="#13a594" stroke-width="1.6" fill="none"/></svg>Home</li>
  <li><svg width="9" height="9" viewBox="0 0 12 12"><path d="M1 6h9M6 2l4 4-4 4" stroke="#13a594" stroke-width="1.6" fill="none"/></svg>About</li>
  <li><svg width="9" height="9" viewBox="0 0 12 12"><path d="M1 6h9M6 2l4 4-4 4" stroke="#13a594" stroke-width="1.6" fill="none"/></svg>Services</li>
  <li><svg width="9" height="9" viewBox="0 0 12 12"><path d="M1 6h9M6 2l4 4-4 4" stroke="#13a594" stroke-width="1.6" fill="none"/></svg>Pages</li>
  <li><svg width="9" height="9" viewBox="0 0 12 12"><path d="M1 6h9M6 2l4 4-4 4" stroke="#13a594" stroke-width="1.6" fill="none"/></svg>Blog</li>
</ul>

<h3 class="footer-head" style="left:869px">Contact Us</h3>
<ul class="footer-list" style="left:869px;top:2842px">
  <li><svg width="10" height="12" viewBox="0 0 10 12"><path d="M5 12 C2 8 0.5 6 0.5 4.5 A4.5 4.5 0 0 1 9.5 4.5 C9.5 6 8 8 5 12Z" fill="#13a594"/><circle cx="5" cy="4.5" r="1.6" fill="#ecf1f1"/></svg>48 Linden Row, Ashford</li>
  <li><svg width="12" height="9" viewBox="0 0 12 9"><rect width="12" height="9" rx="1" fill="#13a594"/><path d="M0.5 0.8 6 5 11.5 0.8" stroke="#ecf1f1" stroke-width="1.2" fill="none"/></svg>hello@quietmeadowcare.com</li>
  <li><svg width="11" height="11" viewBox="0 0 12 12"><path d="M2.5 0.5 5 3 3.8 4.5 C4.5 6 6 7.5 7.5 8.2 L9 7 11.5 9.5 10 11.5 C5 11 1 7 0.5 2Z" fill="#13a594"/></svg>555-014-2290</li>
</ul>
<div class="subscribe">Enter Your Email<b>GO</b></div>

<div class="footer-rule"></div>
<p class="copyright">Copyright 2022 Mara Ellison. All Rights Reserved</p>

</body>
</html>
```